Flyer für kleine christliche Gemeinde
professionelles Vorgehen. pulvrin hat sehr gut Sinn und Konzept unserer Veranstaltung erfasst und den Flyer mit passenden Bildern und angemessener Designgestaltung versehen. Stach aus den anderen Vorschlägen heraus. Änderungswünsche und auch Planänderungen unsererseits wurden geduldig und sehr geschmackvoll umgesetzt. Wer ein fundiertes, modernes und ansprechendes, passendes Design braucht ist mit diesem Designer gut beraten.
Zielgruppe
kleine christliche Gemeinde, Einladung zu einer Vortragsreihe zu aktuellen Themen /Krisen unserer Zeit, Zielgruppe: Erwachse Menschen aller Couleur mit Interesse an aktuellem Zeitgeschehen und Antworten für die Probleme unserer Zeit, Sinn- und Orientierungssuchende, Bibelinteressierte
Aufgabenstellung
Aufmerksamkeit fesselnder, dennoch seriös wirkender, informativer Flyer als Einladung zu einer Vortragsreihe, Verteilung per Hand auf der Straße und in Briefkästen, Information zum Redner kürzen wenn nötig, Anfahrtsskizze und Informationen zu Erreichbarkeit (Bus...), Stockbilder möglichst kostenfreie verwenden,

```html
<!DOCTYPE html>
<html lang="de">
<head>
<meta charset="utf-8">
<title>Warnrufe unserer Zeit – Flyer</title>
<link href="https://fonts.googleapis.com/css2?family=Playfair+Display:wght@600;700&family=Noto+Serif:ital,wght@0,400;0,700;1,400&family=PT+Sans:ital@1&display=swap" rel="stylesheet">
<style>
:root{
  --bg:#e4e4e2;
  --paper:#ffffff;
  --purple:#7b72b3;
  --green:#5e8c3f;
  --red:#a3261c;
  --ink:#222222;
  --night:#20284a;
  --dusk:#8a7f8e;
  --fire:#e89a2a;
  --ember:#3a1d10;
}
*{margin:0;padding:0;box-sizing:border-box}
html,body{width:1200px;height:1200px;overflow:hidden;background:var(--bg)}
body{position:relative;font-family:"Noto Serif",Georgia,serif;color:var(--ink)}

/* Titelseite */
.cover{position:absolute;left:285px;top:30px;width:330px;height:580px;overflow:hidden;color:#fff;text-align:center}
.cover-photo{position:absolute;inset:0;background:linear-gradient(180deg,var(--night) 0%,#4b4f78 18%,var(--dusk) 34%,#d9c8b0 50%,var(--fire) 66%,#b04a18 78%,var(--ember) 90%,#0e0a08 100%)}
.cover-kicker{position:absolute;top:38px;width:100%;font-size:9px;letter-spacing:.3px}
.cover-title{position:absolute;top:52px;left:0;width:100%;font-family:"Playfair Display",Georgia,serif;font-weight:700;line-height:.95;text-shadow:0 2px 4px rgba(0,0,0,.4)}
.cover-title .w1{display:block;font-size:44px}
.cover-title .w2{display:block;font-size:30px}
.cover-title .w3{display:inline-block;font-size:60px;vertical-align:top}
.cover-sub{display:inline-block;font-family:"Noto Serif",Georgia,serif;font-weight:400;font-size:13px;line-height:1.05;text-align:left;vertical-align:top;margin-top:12px;text-shadow:none}
.cover-tag{position:absolute;top:190px;left:0;width:100%;font-size:13px;line-height:1.3;text-align:center}
.cover-series{position:absolute;top:440px;width:100%;font-family:"Playfair Display",Georgia,serif;font-weight:700;font-size:20px;line-height:1.2}
.cover-date{position:absolute;top:505px;left:40px;width:220px;font-family:"Playfair Display",Georgia,serif;font-weight:700;font-size:16px;line-height:1.35}
.cover-badge{position:absolute;right:-40px;bottom:-40px;width:120px;height:120px;border-radius:50%;background:var(--purple);font-family:"Playfair Display",Georgia,serif;font-weight:600;font-size:12px;line-height:1.05;padding:48px 0 0 14px;text-align:left}

/* Rückseite mit Anfahrt */
.directions{position:absolute;left:650px;top:30px;width:300px;height:580px;background:var(--paper);padding:28px 18px 0 20px}
.stops{list-style:none}
.stop{display:flex;gap:8px;font-size:9.4px;line-height:1.4;margin-bottom:14px}
.stop-num{flex:none;width:14px;height:14px;border-radius:50%;background:var(--red);color:#fff;font-size:9px;text-align:center;line-height:14px;margin-top:1px}
.stop-label{color:var(--purple);font-weight:700}
.map{position:absolute;left:18px;top:230px;width:264px;height:320px;background:linear-gradient(135deg,#eef1f5,#dfe5ee 60%,#cfdbe8)}
.map-credit{position:absolute;left:60px;top:556px;font-size:5.5px}

/* Innenseite */
.inside{position:absolute;left:375px;top:622px;width:552px;height:552px;background:var(--paper);display:flex}
.inside-left{width:276px;padding:22px 14px 0 18px;position:relative;font-size:7.4px;line-height:1.45;text-align:justify}
.inside-left p{margin-bottom:9px}
.quote{position:relative;margin:10px 6px 0 52px;font-family:"PT Sans",Arial,sans-serif;font-style:italic;color:var(--red);font-size:8.4px;line-height:1.38;text-align:center}
.quote-mark{position:absolute;font-family:"Playfair Display",Georgia,serif;font-style:normal;font-size:36px;line-height:1}
.quote-mark.open{left:-22px;top:-4px}
.quote-mark.close{right:-22px;bottom:-20px}
.quote-source{display:block;margin:8px 10px 0 0;font-size:5.8px;line-height:1.35;text-align:right;font-style:normal}
.dove{position:absolute;left:38px;top:254px;width:90px;height:88px;background:radial-gradient(ellipse,#f1efea 40%,rgba(241,239,234,0) 72%)}
.questions{position:absolute;left:16px;top:330px;display:flex;gap:6px}
.question{width:76px;height:76px;color:#fff;font-size:7.6px;line-height:1.45;display:flex;align-items:center;justify-content:center;text-align:center;padding:4px}
.question.purple{background:var(--purple)}
.question.low{padding-top:20px}
.question.green{background:var(--green)}
.closing{position:absolute;left:18px;top:425px;width:120px;font-size:7.4px;line-height:1.55;text-align:justify}
.cross-photo{position:absolute;left:155px;top:425px;width:100px;height:100px;background:linear-gradient(180deg,#9fb7b4,#c8d8d0 40%,#59766f 75%,#0d120f)}

.inside-right{width:276px;position:relative}
.storm-photo{position:absolute;left:0;top:0;width:135px;height:136px;background:linear-gradient(180deg,#6e7572,#9aa09a 45%,#6b7a3e 75%,#3f4a24)}
.mask-photo{position:absolute;left:142px;top:142px;width:134px;height:136px;background:linear-gradient(135deg,#8a7a3a,#3c3a2c 50%,#1d1f1a)}
.panel{position:absolute;color:#fff;padding:12px 8px 0 10px}
.panel.p1{left:142px;top:0;width:134px;height:136px;background:var(--purple)}
.panel.p2{left:0;top:142px;width:135px;height:136px;background:var(--green)}
.talk{display:flex;gap:6px;margin-bottom:12px}
.talk-num{font-size:20px;line-height:1;width:18px;flex:none}
.talk-title{font-weight:700;font-size:7.2px;line-height:1.25}
.talk-sub{font-size:6.6px;line-height:1.3}
.speaker{position:absolute;left:0;top:286px;width:276px;height:266px;background:var(--purple);color:#fff;padding:12px 16px 0 16px;font-size:6.2px;line-height:1.45;text-align:justify}
.speaker h3{font-size:7.5px;font-weight:700;line-height:1.2}
.speaker p{margin-bottom:8px}
</style>
</head>
<body>

<section class="cover">
  <div class="cover-photo" role="img" aria-label="Gewitterhimmel mit weißer Taube über einer Explosion und Soldaten-Silhouetten"></div>
  <p class="cover-kicker">Evangelisation mit Daniel</p>
  <h1 class="cover-title">
    <span class="w1">Warnrufe</span>
    <span class="w2">unserer</span>
    <span class="w3">Zeit</span>
    <span class="cover-sub">oder wie wir<br>&nbsp;&nbsp;unsere</span>
  </h1>
  <p class="cover-tag">Freiheit/Individualität<br>verkaufen/verspielen</p>
  <p class="cover-series">Eine Kurz-Serie mit<br>Daniel Moreno</p>
  <p class="cover-date">Pfingsten,<br>17-20. Mai 2024</p>
  <div class="cover-badge">Eintritt<br>&nbsp;&nbsp;&nbsp;frei</div>
</section>

<section class="directions">
  <ol class="stops">
    <li class="stop"><span class="stop-num">1</span><span><span class="stop-label">Veranstaltungsort:</span><br>Kulturzentrum Lindenhof-Haus,<br>Wiesenweg 1, 16500 Havelstadt,<br>Nähe Schloss Havelstadt</span></li>
    <li class="stop"><span class="stop-num">2</span><span>Zugang über Wiesenweg.<br>Der Eingang liegt auf der Rückseite</span></li>
    <li class="stop"><span class="stop-num">3</span><span>Zugang über Lindenallee</span></li>
    <li class="stop"><span class="stop-num">4</span><span>Kostenloser Parkplatz, 6 Gehminuten</span></li>
    <li class="stop"><span class="stop-num">5</span><span>Bushaltestelle Lindenallee Bus 804 u. 824</span></li>
  </ol>
  <div class="map" role="img" aria-label="Anfahrtskarte mit Fußweg von Parkplatz und Bushaltestelle zum Veranstaltungsort"></div>
  <p class="map-credit">Kartendaten © 2024 Kartenwerk Nord</p>
</section>

<section class="inside">
  <div class="inside-left">
    <p>Bedrohungen durch <b>Krieg, Umweltkatastrophen, Klimawandel,</b> zunehmende soziale <b>Unsicherheit/Ungerechtigkeit</b> und <b>Zerfall/Spaltung</b> der Gesellschaft erfüllen uns immer mehr mit Sorgen für die Zukunft. Politiker und die Mächtigen der Welt suchen in Weltwirtschaftsforen und Klimakonferenzen nach Antworten und Lösungswegen globaler Probleme. Wirtschaft, Wissenschaft, Politik und Kirchen suchen nach Orientierung und Führung, geradezu nach einem Erlöser, der die Kräfte für den Rettungsweg unseres Planeten eint.</p>
    <p>Fakenews im Netz, Verschwörungstheorien, aufsehenerregende Berichterstattung und voreilige politische Planspiele steigern die Verunsichern der Menschen. Die tatsächliche Ratlosigkeit der Großen und Mächtigen und die Verunsicherung der Bevölkerung der Welt spiegeln sich dramatisch in folgenden Worten wieder:</p>
    <blockquote class="quote">
      <span class="quote-mark open">“</span>Und es werden Zeichen geschehen an Sonne und Mond und Sternen, und auf Erden Angst der Völker vor Ratlosigkeit bei dem Tosen des Meeres und der Wogen, da die Menschen in Ohnmacht sinken werden vor Furcht und Erwartung dessen, was über den Erdkreis kommen soll; denn die Kräfte des Himmels werden erschüttert werden.<span class="quote-mark close">”</span>
    </blockquote>
    <cite class="quote-source">Die Bibel, Lukas Kapitel 21, Vers 25-26<br>[Übersetzung nach Lindner 2000]</cite>
    <div class="dove" role="img" aria-label="Fliegende weiße Taube"></div>
    <div class="questions">
      <div class="question purple low">Doch wo<br>stehen wir?</div>
      <div class="question green">Wie kommen wir durch die Wirrnisse dieser Zeit?</div>
      <div class="question purple">Welche echten Lösungsansätze gibt es?</div>
    </div>
    <p class="closing">Erfahren Sie Gottes Fahrplan für diese Welt. Lernen Sie den einzigen Ausweg und die Chance kennen, Ihre persönliche Individualität und einen kühlen Kopf zu bewahren und finden echte Sicherheit auf ihrem Weg in/durch unsicheren Zeiten.</p>
    <div class="cross-photo" role="img" aria-label="Drei Kreuze als Silhouette vor lichtdurchflutetem Himmel"></div>
  </div>

  <div class="inside-right">
    <div class="storm-photo" role="img" aria-label="Tornado über einem Feldweg"></div>
    <div class="panel p1">
      <div class="talk"><span class="talk-num">1.</span><div><div class="talk-title">Das Ewige Evangelium-<br>Ein Ausweg</div><div class="talk-sub">Echte Freiheit und Unabhängigkeit<br>(Fr., 17.5., 18:30 Uhr )</div></div></div>
      <div class="talk"><span class="talk-num">2.</span><div><div class="talk-title">Drei fliegende Engel</div><div class="talk-sub">Systeme der Macht-der Kampf um unseren Kopf<br>(Sa., 18.5., 18:30 Uhr)</div></div></div>
    </div>
    <div class="panel p2">
      <div class="talk"><span class="talk-num">3.</span><div><div class="talk-title">Das Siegel Gottes oder das Malzeichen des Tieres</div><div class="talk-sub">Erzwungene/Erpresste Loyalität - wie wir sie zeigen müssen<br>(So., 19.5., 18:30 Uhr)</div></div></div>
      <div class="talk"><span class="talk-num">4.</span><div><div class="talk-title">Text Platzhalter Titel</div><div class="talk-sub">Text Platzhalter Subtitel<br>(Mo., 20.5., 18:30 Uhr)</div></div></div>
    </div>
    <div class="mask-photo" role="img" aria-label="Person mit Gasmaske in gelbem Schutzanzug"></div>
    <div class="speaker">
      <h3>Zum Sprecher:</h3>
      <p>Pastor Daniel Moreno stammt aus Villa Serena, Costa Alba. Als junger Mann trat er in das Priesterseminar San Lucas ein, um Priester zu werden. Auf einer Reise lernte er in Port Ashby, New Carlow, ein Seminar über die Prophezeiungen in Daniel und der Offenbarung kennen. Überzeugt von der Verlässlichkeit der biblischen Prophetie ließ er sich taufen und studierte Theologie an der Universidad del Caribe Oriental in Puerto Claro. Heute leitet er die Living Hope Church, gibt den Hope Boten heraus und spricht jede Woche im Radio.</p>
      <p>Seit mehr als 20 Jahren wirbt er landesweit und im Ausland für ein besseres Verständnis der biblischen Weissagungen. Er nutzt dafür Vorträge, Druckschriften, Plakate, Radiobeiträge, Besuche in Gefängnissen, Missionsreisen und ganzseitige Anzeigen in Zeitungen.</p>
      <p>Mit seinem Wissen über Weltgeschichte, über kulturelle, politische und religiöse Zusammenhänge und über die weitreichenden Prophetien der Bibel, vorgetragen mit lateinamerikanischer Begeisterung, gibt er seinen Zuhörern lebendige und verständliche Einblicke in die Entwicklungen unserer Gesellschaft und ihre Zukunftsperspektiven.</p>
    </div>
  </div>
</section>

</body>
</html>
```